Photo/Video Company needs a business card design

We need a business card design for a photo/video production company called 'Brightwave Studios'. We primarily do wedding photography and videography, however we also do commercial, corporate, and promo work.

We would like a clean, white design that primarily markets us as a wedding photo/video company, but still sleek enough that we attract corporate and commercial clients.

Industry/Entity Type

Wedding

Requirements
Must have
• We wish the front of the business card to simply have the logo, and the back will have the contact information:

Brightwave Studios
Wedding, Event, Corporate, Commercial, Promo
647-518-2736
info@brightwavestudios.example
www.brightwavestudios.example

We are hoping for a version of the card that has only the companies name on it, as well as several variations that have different employees names printed.

The employee names and titles are:

Teo Lindqvar - Photo/Video
Dilan Lindqvar - Photo/Video
Pieter Kalbrook -Video
Odile Brunvik -Photo/Video

The design should use similar fonts in the writing as the fonts used in the logo design. The AI file will be provided.
Nice to have
• We also might like to see the front of the card have the main logo, as well as 'Wedding, Event, Corporate, Commercial, Promo' written in the bottom corner.
Should not have
• No old style fonts should be used. Also no other graphic images should be created, but we are open to the possibility of having shapes and borders.

```html
<!DOCTYPE html>
<html lang="en">
<head>
<meta charset="utf-8">
<title>Brightwave Studios — Business Card</title>
<link href="https://fonts.googleapis.com/css2?family=Questrial&family=Arimo:wght@400&display=swap" rel="stylesheet">
<style>
  :root {
    --backdrop: #e2e2e3;
    --card: #ffffff;
    --card-edge: #d6d6d8;
    --ink: #2b2b2d;
    --ink-soft: #3a3a3c;
    --accent: #b3161b;
    --band-dark: #1c1c1e;
    --band-light: #c9c9cb;
    --band-text: #f2f2f2;
  }
  * { margin: 0; padding: 0; box-sizing: border-box; }
  html, body {
    width: 1200px; height: 765px; overflow: hidden;
    background: var(--backdrop);
  }
  .stage { position: relative; width: 1200px; height: 765px; }
  .card {
    position: absolute; top: 302px;
    width: 575px; height: 343px;
    background: var(--card);
    border: 1px solid var(--card-edge);
    border-radius: 40px;
    overflow: hidden;
    color: var(--ink);
    font-family: "Questrial", sans-serif;
  }
  .card--front { left: 16px; }
  .card--back { left: 604px; }

  .brand { position: absolute; display: flex; align-items: center; }
  .brand__mark { background: var(--accent); flex: none; }
  .brand__name {
    font-family: "Questrial", sans-serif;
    color: var(--ink); text-transform: uppercase; white-space: nowrap;
  }

  .card--front .brand { left: 104px; top: 144px; gap: 16px; }
  .card--front .brand__mark { width: 40px; height: 40px; }
  .card--front .brand__name { font-size: 29px; letter-spacing: 0.5px; }

  .services {
    position: absolute; left: 60px; top: 286px;
    font-size: 9.5px; letter-spacing: 3.6px; color: var(--ink-soft);
    white-space: nowrap;
  }
  .services span { margin: 0 9px; }

  .card--back .brand { left: 46px; top: 148px; gap: 8px; }
  .card--back .brand__mark { width: 18px; height: 18px; }
  .card--back .brand__name { font-size: 14.5px; }

  .person { position: absolute; left: 292px; top: 66px; }
  .person__name { font-family: "Arimo", sans-serif; font-size: 35px; color: var(--ink); line-height: 1; }
  .person__role { font-family: "Arimo", sans-serif; font-size: 15px; color: var(--ink-soft); margin-top: 8px; }

  .service-band {
    position: absolute; left: 257px; top: 146px; width: 318px; height: 21px;
    background: linear-gradient(90deg, var(--band-dark) 0%, var(--band-dark) 45%, var(--band-light) 100%);
    color: var(--band-text);
    font-family: "Arimo", sans-serif; font-size: 8.4px; letter-spacing: 0.3px;
    display: flex; align-items: center; padding-left: 5px; white-space: nowrap;
  }
  .service-band span { margin: 0 4px; }

  .contacts { position: absolute; left: 292px; top: 214px; list-style: none; }
  .contacts li {
    display: flex; align-items: center; gap: 9px; height: 20.5px;
    font-family: "Arimo", sans-serif; font-size: 15.5px; color: var(--ink-soft);
  }
  .contacts svg { width: 16px; height: 16px; flex: none; }
</style>
</head>
<body>
<main class="stage">

  <section class="card card--front" aria-label="Card front">
    <div class="brand">
      <div class="brand__mark"></div>
      <div class="brand__name">Brightwave Studios</div>
    </div>
    <p class="services">WEDDING<span>|</span>EVENT<span>|</span>CORPORATE<span>|</span>COMMERCIAL<span>|</span>PROMO</p>
  </section>

  <section class="card card--back" aria-label="Card back">
    <div class="brand">
      <div class="brand__mark"></div>
      <div class="brand__name">Brightwave Studios</div>
    </div>

    <div class="person">
      <p class="person__name">Teo Lindqvar</p>
      <p class="person__role">Photo/Video</p>
    </div>

    <div class="service-band">WEDDING<span>|</span>EVENT<span>|</span>CORPORATE<span>|</span>COMMERCIAL<span>|</span>PROMO</div>

    <ul class="contacts">
      <li>
        <svg viewBox="0 0 16 16" aria-hidden="true"><rect width="16" height="16" rx="3" fill="#1c1c1e"/><path d="M4 6.5c0-1.3 1.8-2 4-2s4 .7 4 2v.6h-2.2v-.9H6.2v.9H4z" fill="#fff"/><rect x="4.5" y="7.8" width="7" height="4" rx="1" fill="#fff"/><circle cx="8" cy="9.8" r="1" fill="#1c1c1e"/></svg>
        647-518-2736
      </li>
      <li>
        <svg viewBox="0 0 16 16" aria-hidden="true"><rect width="16" height="16" rx="3" fill="#1c1c1e"/><rect x="3.5" y="5" width="9" height="6.5" rx="0.6" fill="#fff"/><path d="M3.8 5.4 8 8.7l4.2-3.3" fill="none" stroke="#1c1c1e" stroke-width="1"/></svg>
        info@brightwavestudios.example
      </li>
      <li>
        <svg viewBox="0 0 16 16" aria-hidden="true"><rect width="16" height="16" rx="3" fill="#1c1c1e"/><g fill="none" stroke="#fff" stroke-width="0.9"><circle cx="8" cy="8" r="4.8"/><ellipse cx="8" cy="8" rx="2" ry="4.8"/><path d="M3.2 8h9.6M4 5.6h8M4 10.4h8"/></g></svg>
        www.brightwavestudios.example
      </li>
    </ul>
  </section>

</main>
</body>
</html>
```